依頼詳細
80-90年代の社会問題や表象をテーマにした市民参加型の調査サークルの部員募集のためのチラシです。
遊び心をもち、裏路地に入っていくことを想起するように、80年代後半~90年代初頭のピンクチラシをモチーフにデザインをお願いします。
記載項目
団体名:かわせみタンボウクラブ部(かわタン)
連絡先:Chatora:https//chatora-link.example/7kQmW2pX

必ず記載してほしい内容は下記です。
・仙台の社会活動を一緒に調査してくれるステキなアナタ!
・ただ今、部員募集!
・自由出勤(委細面接)
・経験者・未経験者
※なんでも、お気軽にご連絡下さい。
サイズ
A5
ページ数
片面
希望イメージ
シンプル 複雑
単色 カラフル
暗い 明るい
日常 高級
遊び心 厳粛
未来的 伝統的
女性的 男性的
希望する色
納品ファイル
• イラストレーター形式 (.ai)
• PNG形式 (.png)
補足説明
■ 選んだ理由

ご提案の内容を汲み取っていただき、活動の参加対象となる方にとって親しみあるデザインでしたので、採用させていただきました。

■ 提案者全員のお礼・コメント

ご提案大変ありがとうございました。難しいテーマにも関わらず、意図を汲み取っていただき、ユニークなご提案を多くいただきました。ご参加いたた皆様、大変ありがとうございました。

```html
<!DOCTYPE html>
<html lang="ja">
<head>
<meta charset="utf-8">
<title>かわタン 部員募集</title>
<link rel="stylesheet" href="https://fonts.googleapis.com/css2?family=Dela+Gothic+One&family=M+PLUS+1p:wght@800;900&display=swap">
<style>
  :root {
    --paper: #f8e81c;
    --ink: #111111;
    --banner: #ffffff;
    --swirl-a: #ff3e9a;
    --swirl-b: #2f6bff;
    --swirl-c: #19c86a;
    --swirl-d: #ffb400;
  }
  * { margin: 0; padding: 0; box-sizing: border-box; }
  html, body { width: 846px; height: 1200px; overflow: hidden; background: var(--paper); }
  .flyer {
    position: relative;
    width: 846px;
    height: 1200px;
    background: var(--paper);
    border: 4px solid var(--ink);
    overflow: hidden;
    color: var(--ink);
    font-family: "M PLUS 1p", sans-serif;
    font-weight: 900;
  }
  .club-name {
    position: absolute;
    left: 150px;
    top: 40px;
    font-size: 38px;
    letter-spacing: 1px;
    white-space: nowrap;
  }
  .club-short {
    position: absolute;
    left: 270px;
    top: 78px;
    font-family: "Dela Gothic One", sans-serif;
    font-size: 108px;
    line-height: 1.1;
    letter-spacing: 4px;
    white-space: nowrap;
  }
  .recruit-banner {
    position: absolute;
    left: 115px;
    top: 222px;
    width: 540px;
    height: 100px;
    background: var(--banner);
    border: 4px solid var(--ink);
    transform: rotate(-4deg);
    display: flex;
    align-items: center;
    justify-content: center;
    font-size: 52px;
    letter-spacing: 2px;
    white-space: nowrap;
  }
  .note {
    position: absolute;
    left: 205px;
    top: 354px;
    font-size: 16px;
    font-weight: 800;
    line-height: 1.5;
    white-space: nowrap;
  }
  .tagline {
    position: absolute;
    right: 24px;
    top: 70px;
    writing-mode: vertical-rl;
    font-size: 37px;
    line-height: 1;
    letter-spacing: 1px;
    white-space: nowrap;
  }
  .conditions {
    position: absolute;
    left: 28px;
    top: 440px;
    writing-mode: vertical-rl;
    font-size: 35px;
    line-height: 1;
    letter-spacing: 0;
    white-space: nowrap;
  }
  .illustration {
    position: absolute;
    left: 110px;
    top: 430px;
    width: 612px;
    height: 766px;
    background:
      radial-gradient(circle at 30% 30%, var(--swirl-a) 0 18%, transparent 40%),
      radial-gradient(circle at 75% 55%, var(--swirl-b) 0 15%, transparent 42%),
      radial-gradient(circle at 25% 80%, var(--swirl-c) 0 14%, transparent 38%),
      linear-gradient(160deg, var(--swirl-d), var(--swirl-a) 45%, var(--swirl-b));
  }
</style>
</head>
<body>
  <main class="flyer">
    <p class="club-name">かわせみタンボウクラブ部</p>
    <h1 class="club-short">かわタン</h1>
    <p class="recruit-banner">ただ今、部員募集！</p>
    <p class="note">※なんでも、お気軽にご連絡下さい。<br>連絡先:Chatora:https//chatora-link.example/7kQmW2pX</p>
    <p class="tagline">仙台の社会活動を一緒に調査してくれるステキなアナタ!</p>
    <p class="conditions">・自由出勤（委細面接）・経験者・未経験者</p>
    <div class="illustration" role="img" aria-label="サイケデリックな渦模様を背景に、金髪にリボンをつけた制服姿の少女のレトロ調イラスト"></div>
  </main>
</body>
</html>
```